Tattoo Shop Business Card

I need a Business Card for the The Harbor Quill.

I'm thinking i want a double sided business card, really clean, very classy, one side the logo, and on the other my information. I'm pretty much open to anything, as long as its fun and captures class and elegance, while at the same time is edgy and tattooish.
I don't want your typical classic card. Add your own twist on it

Logo is attached to this brief

Please include:
Name
Position
Phone Number
Email
Website

Target Market(s)

I'm looking to capture potential clients for my tattoo shop so the card needs to be something they can fit in their wallet but they will also remember me when they see that card in there. My target audience is everyone over 18 that is intrigued by tattoos and piercings.

Industry/Entity Type

Business

Font styles to use
Serif

Colors

Designer to choose colors to be used in the design.

Requirements
Must have
• must be bold and something people will never forget

```html
<!DOCTYPE html>
<html lang="en">
<head>
<meta charset="utf-8">
<title>The Harbor Quill — Business Card</title>
<link rel="stylesheet" href="https://fonts.googleapis.com/css2?family=Playfair+Display+SC:wght@700&family=Kalam:wght@700&family=Saira:wght@500&display=swap">
<style>
  :root {
    --page: #e9e8e6;
    --ink: #0b0b0b;
    --paper: #ffffff;
    --silver: #8e8e8e;
    --flourish-dark: #3a3a3a;
    --flourish-light: #d4d4d4;
    --rule: #222222;
  }
  * { box-sizing: border-box; margin: 0; padding: 0; }
  html, body { width: 1200px; height: 1200px; overflow: hidden; }
  body { background: var(--page); position: relative; }

  .card {
    position: absolute;
    width: 660px;
    height: 390px;
    border-radius: 16px;
    overflow: hidden;
    box-shadow: 0 12px 30px rgba(0,0,0,0.18);
  }
  .card--front { left: 150px; top: 110px; background: var(--ink); }
  .card--back { left: 390px; top: 640px; background: var(--paper); }

  .flourish { position: absolute; width: 150px; height: 150px; }
  .card--front .flourish { background: radial-gradient(circle at var(--corner), var(--flourish-dark) 0%, rgba(58,58,58,0) 70%); }
  .card--back .flourish { background: radial-gradient(circle at var(--corner), var(--flourish-light) 0%, rgba(212,212,212,0) 70%); }
  .flourish--tl { left: 0; top: 0; --corner: 0 0; }
  .flourish--tr { right: 0; top: 0; --corner: 100% 0; }
  .flourish--bl { left: 0; bottom: 0; --corner: 0 100%; }
  .flourish--br { right: 0; bottom: 0; --corner: 100% 100%; }

  .brand-name {
    font-family: "Playfair Display SC", Georgia, serif;
    font-weight: 700;
    letter-spacing: 1px;
    text-align: center;
    position: absolute;
    left: 0; right: 0;
  }
  .card--front .brand-name { color: var(--silver); font-size: 60px; top: 150px; }
  .card--back .brand-name { color: var(--ink); font-size: 34px; top: 44px; }

  .holder-name {
    position: absolute;
    left: 190px; top: 100px;
    font-family: "Kalam", cursive;
    font-weight: 700;
    font-size: 56px;
    color: var(--ink);
  }
  .position-rule {
    position: absolute;
    left: 200px; top: 188px;
    width: 330px; height: 2px;
    background: var(--rule);
  }
  .position-tag {
    position: absolute;
    left: 290px; top: 176px;
    width: 230px; height: 28px;
    background: var(--ink);
    color: var(--paper);
    border-radius: 4px;
    font-family: "Saira", sans-serif;
    font-weight: 500;
    font-size: 18px;
    line-height: 28px;
    text-align: center;
    letter-spacing: 0.5px;
  }
  .contact-list {
    position: absolute;
    left: 200px; top: 220px;
    width: 240px;
    list-style: none;
    font-family: "Saira", sans-serif;
    font-weight: 500;
    font-size: 16px;
    color: var(--ink);
  }
  .contact-list li {
    display: flex;
    align-items: center;
    gap: 10px;
    height: 30px;
    border-bottom: 2px dotted var(--rule);
    white-space: nowrap;
  }
  .contact-list svg { width: 16px; height: 16px; flex: none; }
</style>
</head>
<body>

  <section class="card card--front" aria-label="Card front">
    <div class="flourish flourish--tl" role="img" aria-label="Decorative corner flourish"></div>
    <div class="flourish flourish--tr" role="img" aria-label="Decorative corner flourish"></div>
    <div class="flourish flourish--bl" role="img" aria-label="Decorative corner flourish"></div>
    <div class="flourish flourish--br" role="img" aria-label="Decorative corner flourish"></div>
    <h1 class="brand-name">The Harbor Quill</h1>
  </section>

  <section class="card card--back" aria-label="Card back">
    <div class="flourish flourish--tl" role="img" aria-label="Decorative corner flourish"></div>
    <div class="flourish flourish--tr" role="img" aria-label="Decorative corner flourish"></div>
    <div class="flourish flourish--bl" role="img" aria-label="Decorative corner flourish"></div>
    <div class="flourish flourish--br" role="img" aria-label="Decorative corner flourish"></div>
    <h2 class="brand-name">The Harbor Quill</h2>
    <p class="holder-name">Miles Carver</p>
    <div class="position-rule"></div>
    <p class="position-tag">YOUR POSITION</p>
    <ul class="contact-list">
      <li>
        <svg viewBox="0 0 16 16" aria-hidden="true"><path d="M4 1 L6.5 4 L5 6 Q6.5 9.5 10 11 L12 9.5 L15 12 L13 15 Q3 13 1 3 Z" fill="none" stroke="#0b0b0b" stroke-width="1.4" stroke-linejoin="round"/></svg>
        +123 555 0147
      </li>
      <li>
        <svg viewBox="0 0 16 16" aria-hidden="true"><rect x="1" y="3" width="14" height="10" fill="#0b0b0b"/><path d="M1 3 L8 9 L15 3" fill="none" stroke="#fff" stroke-width="1.2"/></svg>
        MILESCARVER@MAIL.COM
      </li>
      <li>
        <svg viewBox="0 0 16 16" aria-hidden="true"><rect x="1.5" y="2" width="13" height="9" fill="none" stroke="#0b0b0b" stroke-width="1.4"/><path d="M5 14 H11 M8 11 V14" stroke="#0b0b0b" stroke-width="1.4"/></svg>
        WWW.THEHARBORQUILL.COM
      </li>
    </ul>
  </section>

</body>
</html>
```